signboard Pranmeko

Hi, We are a language school and we register students abroad in Germany. We-have a lot of department and we need a signboard For Each department so students can Distinguish Each department. The design is the Sámi for all the departments. Only texts changes. List of departments: - Visa - Pre-university enrollment - Translations - Language school - Sales We need a Design that respect our logo colors, with our logo Thank u Waiting for proposals

Industry/Entity Type

School

```html
<!DOCTYPE html>
<html lang="fr">
<head>
<meta charset="utf-8">
<title>Signalétique des départements</title>
<link rel="stylesheet" href="https://fonts.googleapis.com/css2?family=Barlow:wght@600;700;800&family=Barlow+Condensed:wght@600;700&display=swap">
<style>
  :root {
    --backdrop: #b8922f;
    --sign-yellow: #d6d82a;
    --sign-white: #ffffff;
    --ink: #1d1d1b;
  }
  html, body {
    margin: 0;
    padding: 0;
    overflow: hidden;
  }
  body {
    width: 1200px;
    height: 661px;
    background: var(--backdrop);
    position: relative;
    font-family: "Barlow", "Arial Narrow", sans-serif;
  }
  .sign {
    position: absolute;
    width: 376px;
    height: 264px;
    display: block;
  }
  .sign--visa        { left: 16px;  top: 20px; }
  .sign--preinscr    { left: 410px; top: 20px; }
  .sign--ventes      { left: 805px; top: 20px; }
  .sign--traductions { left: 16px;  top: 312px; }
  .sign--ecole       { left: 410px; top: 312px; }
  .sign--ecole-alt   { left: 805px; top: 312px; }

  .sign__tile   { fill: var(--sign-white); }
  .sign__header { fill: var(--sign-yellow); stroke: var(--ink); stroke-width: 4; }
  .sign__panel  { fill: var(--sign-white); stroke: var(--ink); stroke-width: 4; }
  .sign__rule   { fill: var(--ink); }
  .sign__chevron { fill: var(--ink); }
  .sign__label {
    font-family: "Barlow Condensed", sans-serif;
    font-weight: 700;
    font-size: 54px;
    fill: var(--sign-white);
    stroke: var(--ink);
    stroke-width: 5;
    stroke-linejoin: round;
    paint-order: stroke;
  }
  .sign__title {
    font-family: "Barlow", sans-serif;
    font-weight: 800;
    fill: var(--ink);
  }
  .sign__title--light { font-weight: 600; }

  .sign--ecole-alt .sign__header { fill: var(--sign-white); }
  .sign--ecole-alt .sign__panel  { fill: var(--sign-yellow); }
  .sign--ecole-alt .sign__label  { fill: var(--sign-yellow); }
  .sign--ecole-alt .sign__title {
    fill: var(--sign-white);
    stroke: var(--ink);
    stroke-width: 6;
    stroke-linejoin: round;
    paint-order: stroke;
  }

  .caption {
    position: absolute;
    margin: 0;
    font-family: "Barlow Condensed", "Arial Narrow", sans-serif;
    font-weight: 700;
    font-size: 31px;
    line-height: 1;
    color: var(--ink);
    letter-spacing: -0.6px;
    white-space: nowrap;
  }
  .caption--scalable { left: 93px;  top: 582px; }
  .caption--alternate { left: 899px; top: 582px; }
  .caption__accent { color: var(--sign-yellow); }
</style>
</head>
<body>

<svg class="sign sign--visa" viewBox="0 0 470 330" aria-label="Panneau département Visa">
  <rect class="sign__tile" width="470" height="330"/>
  <path class="sign__header" d="M5 80 V20 Q5 6 19 6 H452 Q466 6 466 20 V80 Z"/>
  <rect class="sign__rule" x="0" y="83" width="470" height="4"/>
  <rect class="sign__rule" x="0" y="93" width="470" height="5"/>
  <rect class="sign__rule" x="0" y="102" width="470" height="3"/>
  <path class="sign__panel" d="M6 113 H464 V312 Q464 326 450 326 H20 Q6 326 6 312 Z"/>
  <text class="sign__label" x="22" y="64" textLength="370" lengthAdjust="spacing">DEPARTEMENT</text>
  <path class="sign__chevron" d="M401 24 H418 L440 44 L418 64 H401 L423 44 Z M421 24 H430 L452 44 L430 64 H421 L443 44 Z"/>
  <text class="sign__title" x="235" y="285" font-size="192" text-anchor="middle" textLength="405" lengthAdjust="spacingAndGlyphs">VISA</text>
</svg>

<svg class="sign sign--preinscr" viewBox="0 0 470 330" aria-label="Panneau département Pré-inscriptions universitaires">
  <rect class="sign__tile" width="470" height="330"/>
  <path class="sign__header" d="M5 80 V20 Q5 6 19 6 H452 Q466 6 466 20 V80 Z"/>
  <rect class="sign__rule" x="0" y="83" width="470" height="4"/>
  <rect class="sign__rule" x="0" y="93" width="470" height="5"/>
  <rect class="sign__rule" x="0" y="102" width="470" height="3"/>
  <path class="sign__panel" d="M6 113 H464 V312 Q464 326 450 326 H20 Q6 326 6 312 Z"/>
  <text class="sign__label" x="22" y="64" textLength="370" lengthAdjust="spacing">DEPARTEMENT</text>
  <path class="sign__chevron" d="M401 24 H418 L440 44 L418 64 H401 L423 44 Z M421 24 H430 L452 44 L430 64 H421 L443 44 Z"/>
  <text class="sign__title sign__title--light" x="235" y="203" font-size="60" text-anchor="middle" textLength="425" lengthAdjust="spacingAndGlyphs">PRÉ-INSCRIPTIONS</text>
  <text class="sign__title" x="235" y="267" font-size="60" text-anchor="middle" textLength="432" lengthAdjust="spacingAndGlyphs">UNIVERSITAIRES</text>
</svg>

<svg class="sign sign--ventes" viewBox="0 0 470 330" aria-label="Panneau département Ventes">
  <rect class="sign__tile" width="470" height="330"/>
  <path class="sign__header" d="M5 80 V20 Q5 6 19 6 H452 Q466 6 466 20 V80 Z"/>
  <rect class="sign__rule" x="0" y="83" width="470" height="4"/>
  <rect class="sign__rule" x="0" y="93" width="470" height="5"/>
  <rect class="sign__rule" x="0" y="102" width="470" height="3"/>
  <path class="sign__panel" d="M6 113 H464 V312 Q464 326 450 326 H20 Q6 326 6 312 Z"/>
  <text class="sign__label" x="22" y="64" textLength="370" lengthAdjust="spacing">DEPARTEMENT</text>
  <path class="sign__chevron" d="M401 24 H418 L440 44 L418 64 H401 L423 44 Z M421 24 H430 L452 44 L430 64 H421 L443 44 Z"/>
  <text class="sign__title" x="233" y="260" font-size="128" text-anchor="middle" textLength="440" lengthAdjust="spacingAndGlyphs">VENTES</text>
</svg>

<svg class="sign sign--traductions" viewBox="0 0 470 330" aria-label="Panneau département Traductions">
  <rect class="sign__tile" width="470" height="330"/>
  <path class="sign__header" d="M5 80 V20 Q5 6 19 6 H452 Q466 6 466 20 V80 Z"/>
  <rect class="sign__rule" x="0" y="83" width="470" height="4"/>
  <rect class="sign__rule" x="0" y="93" width="470" height="5"/>
  <rect class="sign__rule" x="0" y="102" width="470" height="3"/>
  <path class="sign__panel" d="M6 113 H464 V312 Q464 326 450 326 H20 Q6 326 6 312 Z"/>
  <text class="sign__label" x="22" y="64" textLength="370" lengthAdjust="spacing">DEPARTEMENT</text>
  <path class="sign__chevron" d="M401 24 H418 L440 44 L418 64 H401 L423 44 Z M421 24 H430 L452 44 L430 64 H421 L443 44 Z"/>
  <text class="sign__title" x="234" y="242" font-size="74" text-anchor="middle" textLength="437" lengthAdjust="spacingAndGlyphs">TRADUCTIONS</text>
</svg>

<svg class="sign sign--ecole" viewBox="0 0 470 330" aria-label="Panneau département École de langue">
  <rect class="sign__tile" width="470" height="330"/>
  <path class="sign__header" d="M5 80 V20 Q5 6 19 6 H452 Q466 6 466 20 V80 Z"/>
  <rect class="sign__rule" x="0" y="83" width="470" height="4"/>
  <rect class="sign__rule" x="0" y="93" width="470" height="5"/>
  <rect class="sign__rule" x="0" y="102" width="470" height="3"/>
  <path class="sign__panel" d="M6 113 H464 V312 Q464 326 450 326 H20 Q6 326 6 312 Z"/>
  <text class="sign__label" x="22" y="64" textLength="370" lengthAdjust="spacing">DEPARTEMENT</text>
  <path class="sign__chevron" d="M401 24 H418 L440 44 L418 64 H401 L423 44 Z M421 24 H430 L452 44 L430 64 H421 L443 44 Z"/>
  <text class="sign__title sign__title--light" x="235" y="205" font-size="99" text-anchor="middle" textLength="385" lengthAdjust="spacingAndGlyphs">ECOLE DE</text>
  <text class="sign__title" x="238" y="305" font-size="118" text-anchor="middle" textLength="410" lengthAdjust="spacingAndGlyphs">LANGUE</text>
</svg>

<svg class="sign sign--ecole-alt" viewBox="0 0 470 330" aria-label="Panneau département École de langue, variante couleur">
  <rect class="sign__tile" width="470" height="330"/>
  <path class="sign__header" d="M5 80 V20 Q5 6 19 6 H452 Q466 6 466 20 V80 Z"/>
  <rect class="sign__rule" x="0" y="83" width="470" height="4"/>
  <rect class="sign__rule" x="0" y="93" width="470" height="5"/>
  <rect class="sign__rule" x="0" y="102" width="470" height="3"/>
  <path class="sign__panel" d="M6 113 H464 V312 Q464 326 450 326 H20 Q6 326 6 312 Z"/>
  <text class="sign__label" x="22" y="64" textLength="370" lengthAdjust="spacing">DEPARTEMENT</text>
  <path class="sign__chevron" d="M401 24 H418 L440 44 L418 64 H401 L423 44 Z M421 24 H430 L452 44 L430 64 H421 L443 44 Z"/>
  <text class="sign__title sign__title--light" x="235" y="205" font-size="99" text-anchor="middle" textLength="385" lengthAdjust="spacingAndGlyphs">ECOLE DE</text>
  <text class="sign__title" x="238" y="305" font-size="118" text-anchor="middle" textLength="410" lengthAdjust="spacingAndGlyphs">LANGUE</text>
</svg>

<p class="caption caption--scalable">Vector design, scalable to any size</p>
<p class="caption caption--alternate">alternate <span class="caption__accent">colour</span> option</p>

</body>
</html>
```